Brightfield Systems Business Cards

We need a new business card design for an Electrical company that also focuses on Audio Visual and Communications. We would like to see designs using our new company logo attached. The cards are for two different people outlined below. Full contact details will be provided when design winner is awarded, use generic information for now. Business card is to be double sided and we are open to layout and design ideas.

Target Market(s)

Residential & Commercial

Industry/Entity Type

Electrical

Contact Information for Business Card

Name: Corwin Blake - Senior Electrician, Name: Felix Wade - Technology Specialist.

Font styles to use
Sans Serif

Colors
0555a3
ffffff
000000

Requirements
Must have
• mobile number, email address, website address, PO Box address,
• A main heading somewhere on the card stating ELECTRICAL SERVICES - AUDIO VISUAL SALES & INSTALLATION - COMMUNICATIONS

```html
<!DOCTYPE html>
<html lang="en">
<head>
<meta charset="utf-8">
<title>Brightfield Systems — Business Cards</title>
<link rel="stylesheet" href="https://fonts.googleapis.com/css2?family=Questrial&display=swap">
<style>
  :root {
    --brand-blue: #0555a3;
    --brand-blue-deep: #0f4a85;
    --brand-blue-soft: #2a66a6;
    --card-white: #ffffff;
    --ink-blue: #1f5a94;
    --page-bg: #e9ebee;
    --text-white: #ffffff;
  }
  * { margin: 0; padding: 0; box-sizing: border-box; }
  html, body {
    width: 1200px;
    height: 900px;
    overflow: hidden;
    background: var(--page-bg);
    font-family: "Questrial", "Century Gothic", sans-serif;
  }
  .canvas {
    position: relative;
    width: 1200px;
    height: 900px;
    display: flex;
    flex-direction: column;
    align-items: center;
    justify-content: center;
    gap: 40px;
  }
  .card {
    position: relative;
    width: 700px;
    height: 400px;
    border-radius: 4px;
    box-shadow: 0 6px 18px rgba(0, 0, 0, 0.18);
    overflow: hidden;
  }

  /* Back side */
  .card--back {
    background: radial-gradient(ellipse at 50% 40%, var(--brand-blue-soft) 0%, var(--brand-blue) 55%, var(--brand-blue-deep) 100%);
    display: flex;
    flex-direction: column;
    align-items: center;
    justify-content: center;
  }
  .brand {
    display: flex;
    flex-direction: column;
    align-items: center;
    gap: 14px;
  }
  .brand--back { color: var(--text-white); }
  .brand__dot {
    width: 58px;
    height: 58px;
    border-radius: 50%;
    background: var(--text-white);
  }
  .brand__name {
    font-size: 50px;
    letter-spacing: 2px;
    line-height: 1;
    text-transform: uppercase;
    text-align: center;
  }
  .brand__name span { display: block; font-size: 30px; letter-spacing: 6px; margin-top: 6px; }

  .services {
    position: absolute;
    left: 0;
    right: 0;
    bottom: 44px;
    text-align: center;
    color: var(--text-white);
    font-size: 15px;
    letter-spacing: 1.5px;
    text-transform: uppercase;
  }

  /* Front side */
  .card--front { background: var(--card-white); }
  .brand--front {
    position: absolute;
    top: 38px;
    left: 0;
    right: 0;
    gap: 10px;
    color: var(--ink-blue);
  }
  .brand--front .brand__dot { width: 40px; height: 40px; background: var(--ink-blue); }
  .brand--front .brand__name { font-size: 34px; }
  .brand--front .brand__name span { font-size: 20px; letter-spacing: 5px; margin-top: 4px; }

  .person {
    position: absolute;
    left: 44px;
    top: 178px;
    color: var(--ink-blue);
    font-size: 22px;
    line-height: 1.15;
  }
  .contact-list {
    position: absolute;
    left: 44px;
    top: 240px;
    list-style: none;
    display: flex;
    flex-direction: column;
    align-items: flex-start;
    gap: 7px;
  }
  .contact-list__item {
    display: inline-block;
    background: var(--ink-blue);
    color: var(--text-white);
    font-size: 16px;
    padding: 3px 22px 3px 6px;
    line-height: 1.1;
    white-space: nowrap;
  }

  .baseline {
    position: absolute;
    left: 22px;
    right: 22px;
    bottom: 28px;
    height: 8px;
  }
</style>
</head>
<body>
<main class="canvas">

  <section class="card card--back" aria-label="Business card back">
    <div class="brand brand--back">
      <div class="brand__dot"></div>
      <div class="brand__name">Brightfield<span>Systems</span></div>
    </div>
    <p class="services">Electrical Services - Audio Visual Sales &amp; Installation - Communications</p>
  </section>

  <section class="card card--front" aria-label="Business card front">
    <div class="brand brand--front">
      <div class="brand__dot"></div>
      <div class="brand__name">Brightfield<span>Systems</span></div>
    </div>

    <div class="person">
      <p class="person__name">Corwin Blake</p>
      <p class="person__role">Senior Electrician</p>
    </div>

    <ul class="contact-list">
      <li><span class="contact-list__item">0400 555 826</span></li>
      <li><span class="contact-list__item">PO Box 1234, your city.</span></li>
      <li><span class="contact-list__item">youremail.com</span></li>
      <li><span class="contact-list__item">www.yoursite.com</span></li>
    </ul>

    <svg class="baseline" viewBox="0 0 656 8" preserveAspectRatio="none" aria-hidden="true">
      <line x1="0" y1="2" x2="656" y2="2" stroke="#1f5a94" stroke-width="2"/>
      <rect x="300" y="3" width="356" height="5" fill="#1f5a94"/>
    </svg>
  </section>

</main>
</body>
</html>
```